UI design for Fast Food Restaurant Self-Order App

Background:
App purpose: for fast food restaurant customers to self order food/drink by choosing item image, and make payment by tapping the credit card on the card terminal.
Reference: https://www.brivalotech.example/product-overview/self-order-kiosks/
Attachment:
Wireframes. (wire frames provide general idea and the information to display, they are not a strict guideline for layout design.)
Pollardo's Self ordering app.
Intro:
We have built a (for restaurant and cafe) Self Ordering and Payment app, similar to Pollardo's self ordering software in most of their new restaurants. Our app will be placed in a Quorvex Panes 10 OS touch screen Kiosk(screen size 4:3 or Portrait 16:9) within the restaurant/cafe premise.
Pages to be designed:
Page 1. Food Browsing Page. displays all food images(to be provided by cafes) by categories, and displays the Cart. This page will lead to Page 2 or Page 3.
'Cart' section should include:
'cart items/selected items', its quantity and price. like Pollardos' app.
When click on a Cart Item, we need to allow to change quantity or 'change Choice'. The UI handling these change requests with ease will be one deciding factor for us to choose your design.
Fact: up to 10 food categories, and 10 - 25 food items under each categories.
When click on one item image, it goes to Page 2.
Page 2. Item Detail/Description Page. Shows description of the food, and its available Choice(other food items or Special Request, up to 12) will also be displayed. 'Add item to cart' action(Button Name: ADD) will happen here and go back to Browsing Page 1.
e.g. Item 'Fried Rice' Page. the Choice could be 'Add Egg', 'Add Meat', 'No Chilli' etc.
Page 3. Order Review Page. No edit features allowed on this page, only two buttons: 'No' to go back to Browsing Page, or 'Yes' to proceed to Payment Page 4. Check Pollardo's screen.
Page 4. Payment Page - Prompt user to Insert or Tap credit card on the credit card terminal. (Exact wording: PLEASE FOLLOW INSTRUCTIONS DISPLAYED ON CREDIT CARD TERMINAL BELOW)
Page 5. Payment status. Successful / Failed.
Our considerations to pick the winner:
1. In terms of design for this task, we look out for page layout, effects, fonts, button style and overall colour scheme. the design should present itself in a clean and modern look, with minimum clicking or scrolling. The app aims to help customers choose and pay for their items quickly.
2.we need to handle both 4:3(as shown in wire frames) and 16:9 screens(like Pollardo's). there will be a lot more vertical space to utilise when it is in 16:9, resulting less scrolling than 4:3. tell us what you think.
All questions are welcome.
Winner has opportunity to work on a few more app UI. Cheers!
Industry/Entity Type
Fast Food Restaurant
Requirements
Must have
- Button colour differentiation - helps people know what to click next.
- best use of screen space. minimum click and scrolls.
Nice to have
- any personal touch.
Should not have
- unrelated design pattern, e.g. a cute animal or flower pattern in the layout.

```html
<!DOCTYPE html>
<html lang="en">
<head>
<meta charset="utf-8">
<title>Self-Order Kiosk – Main Menu</title>
<link href="https://fonts.googleapis.com/css2?family=Comfortaa:wght@500;700&display=swap" rel="stylesheet">
<style>
  :root{
    --orange:#f26a2e;
    --orange-light:#f79a5a;
    --red:#d9151e;
    --price-red:#c8102e;
    --green:#1fb43a;
    --yellow:#f7b500;
    --ink:#1e1e1e;
    --muted:#777;
    --line:#dcdcdc;
    --panel-grey:#ececec;
    --bg:#ffffff;
  }
  *{box-sizing:border-box;margin:0;padding:0}
  html,body{width:1200px;height:979px;overflow:hidden;background:var(--bg)}
  body{font-family:"Comfortaa",sans-serif;color:var(--ink)}
  .kiosk{position:relative;width:1200px;height:979px;background:var(--bg)}

  .menu-band{position:absolute;left:240px;top:40px;width:960px;height:52px;border-radius:26px 0 0 26px;
    background:linear-gradient(90deg,var(--orange-light),var(--orange));box-shadow:0 4px 10px rgba(242,106,46,.35)}
  .menu-band h1{color:#fff;font-size:20px;font-weight:700;line-height:52px;padding-left:28px}

  .sidebar{position:absolute;left:0;top:110px;width:220px}
  .brand-mark{width:84px;height:84px;border-radius:50%;background:var(--orange);margin:0 0 40px 70px;
    border:4px solid #fff;box-shadow:0 0 0 3px var(--orange)}
  .sidebar h2{font-size:17px;font-weight:700;padding-left:36px;margin-bottom:14px}
  .category{display:block;width:190px;height:46px;margin-bottom:12px;border-radius:0 23px 23px 0;background:#fff;
    box-shadow:0 3px 8px rgba(0,0,0,.18);font-size:14px;line-height:46px;padding-left:30px}
  .category.active{background:var(--orange);color:#fff;font-weight:700}

  .menu-grid{position:absolute;left:250px;top:120px;width:640px;display:grid;grid-template-columns:repeat(3,200px);
    column-gap:15px;row-gap:26px}
  .dish-photo{height:160px;border-radius:18px}
  .dish h3{font-size:14px;font-weight:700;margin-top:12px;line-height:1.35}
  .dish .price{color:var(--price-red);font-size:12px;font-weight:700;margin-top:4px}
  .tone-pasta{background:radial-gradient(circle,#d9803a 0,#f3dca0 45%,#f4f0ea 72%)}
  .tone-pizza{background:radial-gradient(circle,#e2513a 0,#e9b466 55%,#f6efe4 75%)}
  .tone-fries{background:radial-gradient(circle,#f3c13a 0,#f5d982 50%,#f7f3e8 75%)}
  .tone-chicken{background:radial-gradient(circle,#b45a1c 0,#cf8a3c 45%,#eef0ea 75%)}
  .tone-beef{background:radial-gradient(circle,#7a3a2a 0,#9b5a46 45%,#f2ece8 75%)}
  .tone-prawn{background:radial-gradient(circle,#ef7a3a 0,#79b944 55%,#f1f5ec 78%)}
  .tone-corn{background:radial-gradient(circle,#f2c82a 0,#f6de6e 50%,#fbf7e6 75%)}
  .tone-pork{background:radial-gradient(circle,#9a7a4a 0,#6fa845 55%,#f0f3ec 78%)}
  .tone-salmon{background:radial-gradient(circle,#f08a5a 0,#7fb949 58%,#f1f5ec 78%)}

  .scroll-track{position:absolute;left:900px;top:400px;width:6px;height:120px;border-radius:3px;background:#d5d5d5}

  .orders{position:absolute;left:920px;top:110px;width:265px;height:800px;background:#fff;
    box-shadow:0 4px 18px rgba(0,0,0,.18);padding:26px 18px}
  .orders h2{font-size:20px;font-weight:700}
  .orders .hint{font-size:10px;color:var(--muted);margin-top:4px;padding-bottom:10px;border-bottom:1px solid var(--line)}
  .order-row{display:grid;grid-template-columns:1fr 30px 56px;font-size:13px;padding:14px 0;border-bottom:1px solid var(--line);align-items:center}
  .order-row .qty{text-align:center}
  .order-row .amount{text-align:right;color:var(--price-red)}
  .order-head{font-weight:700;font-size:13px}
  .order-head .amount{color:var(--ink)}
  .order-row.selected{background:var(--panel-grey);margin:6px -18px;padding:16px 18px;grid-template-columns:1fr 56px;border:none}
  .edit-actions{grid-column:1/-1;display:flex;gap:8px;align-items:center;margin-top:12px}
  .pill{border-radius:14px;height:26px;line-height:26px;padding:0 14px;font-size:11px;font-weight:700;color:#fff}
  .pill.remove{background:var(--red)}
  .pill.change{background:var(--yellow)}
  .stepper{display:flex;margin-left:auto;height:26px;border-radius:4px;overflow:hidden;border:1px solid #444}
  .stepper span{width:24px;text-align:center;line-height:24px;font-size:14px;background:#fff}
  .stepper .btn{background:#333;color:#fff;font-weight:700}
  .divider{border-top:3px double #bbb;margin:26px 0 30px}
  .total{display:flex;justify-content:space-between;align-items:baseline}
  .total .label{font-size:20px;font-weight:700}
  .total .sum{font-size:22px;font-weight:700;color:var(--price-red)}
  .order-actions{position:absolute;left:18px;right:18px;bottom:30px;display:flex;gap:16px}
  .action{flex:1;height:44px;border-radius:22px;color:#fff;font-weight:700;font-size:16px;text-align:center;line-height:44px;
    box-shadow:0 4px 8px rgba(0,0,0,.2)}
  .action.cancel{background:var(--red)}
  .action.order{background:var(--green)}
</style>
</head>
<body>
<main class="kiosk">
  <header class="menu-band"><h1>Main Menu</h1></header>

  <nav class="sidebar">
    <div class="brand-mark"></div>
    <h2>Categories</h2>
    <span class="category">Christmas</span>
    <span class="category">Mini Cakes</span>
    <span class="category">Whole Cakes</span>
    <span class="category active">Main Menu</span>
    <span class="category">Add Ons</span>
    <span class="category">Hot Beverages</span>
  </nav>

  <section class="menu-grid">
    <article class="dish"><div class="dish-photo tone-pasta" role="img" aria-label="Plate of spaghetti with meat sauce"></div><h3>Sunday Meat Spaghetti</h3><p class="price">$10.49</p></article>
    <article class="dish"><div class="dish-photo tone-pizza" role="img" aria-label="Whole pizza with toppings"></div><h3>Crusty Pepperoni Pie</h3><p class="price">$25.00</p></article>
    <article class="dish"><div class="dish-photo tone-fries" role="img" aria-label="French fries with dipping sauce"></div><h3>Golden Heap of Fries</h3><p class="price">$5.49</p></article>
    <article class="dish"><div class="dish-photo tone-chicken" role="img" aria-label="Roast chicken on a plate"></div><h3>Roast Chicken</h3><p class="price">$20.00</p></article>
    <article class="dish"><div class="dish-photo tone-beef" role="img" aria-label="Grilled beef steak"></div><h3>Big Grilled Beefsteak</h3><p class="price">$12.49</p></article>
    <article class="dish"><div class="dish-photo tone-prawn" role="img" aria-label="Baked prawns on lettuce"></div><h3>Sunset Garlic Baked Prawn</h3><p class="price">$10.49</p></article>
    <article class="dish"><div class="dish-photo tone-corn" role="img" aria-label="Corn on the cob"></div><h3>Sweet Corn Cobs</h3><p class="price">$3.50</p></article>
    <article class="dish"><div class="dish-photo tone-pork" role="img" aria-label="Pork dish with vegetables"></div><h3>Herb Pork Platter</h3><p class="price">$9.20</p></article>
    <article class="dish"><div class="dish-photo tone-salmon" role="img" aria-label="Salmon steak with lemon"></div><h3>Salmon Steak Plate</h3><p class="price">$10.30</p></article>
  </section>

  <div class="scroll-track"></div>

  <aside class="orders">
    <h2>Your Orders</h2>
    <p class="hint">Tap an order to change or remove</p>
    <div class="order-row order-head"><span>Item</span><span class="qty">Qty</span><span class="amount">Price</span></div>
    <div class="order-row"><span>Salmon Steak Plate</span><span class="qty">1</span><span class="amount">10.30</span></div>
    <div class="order-row"><span>Roast Chicken</span><span class="qty">1</span><span class="amount">20.00</span></div>
    <div class="order-row selected">
      <span>Herb Pork Platter</span><span class="amount">9.20</span>
      <div class="edit-actions">
        <span class="pill remove">Remove</span>
        <span class="pill change">Change</span>
        <div class="stepper"><span class="btn">−</span><span>1</span><span class="btn">+</span></div>
      </div>
    </div>
    <div class="order-row"><span>Sweet Corn Cobs</span><span class="qty">2</span><span class="amount">7.00</span></div>
    <div class="divider"></div>
    <div class="total"><span class="label">Total</span><span class="sum">$46.50</span></div>
    <div class="order-actions">
      <span class="action cancel">Cancel</span>
      <span class="action order">Order</span>
    </div>
  </aside>
</main>
</body>
</html>
```